PitchTally Webpages and Logo

See attached brief. Take the existing website www.pitchtally.co.uk and logo and transform these assets to:

Give people who arrive on the site for first time the confidence to sign-up easily and quickly
Allow regular returning users quick and easy placing of predictions and encourage them to share the PitchTally prediction on social networks and with their contacts
Convey the essence of a community working together to enjoyably come-up with smart predictions on sporting events
Work seamlessly and well across smartphones, tablets and desktop i.e. Should be Responsive Web Design
Updates

Target Market(s)

Users are sports fans with opinions
Primarily male and early twenties to mid-thirties
They are competitive - they want to beat their peers
Many are from outside the UK

Industry/Entity Type

Events

Logo Text

PitchTally

Coding

Coded - Design and coding required

Number of Pages Required

4 page

Font styles to use
Sans Serif

Requirements
Must have
• Responsive Web Design
• Mobile First
• HTML must work with dedicated bespoke application developed in ASP.NET using MS SQL underneath
• See Brief
Nice to have
• See brief
Should not have
• See brief

```html
<!DOCTYPE html>
<html lang="en">
<head>
<meta charset="utf-8">
<title>PitchTally – Altogether Better Predictions</title>
<link href="https://fonts.googleapis.com/css2?family=Lilita+One&family=Raleway:wght@400;500;600&family=Open+Sans:wght@400;600;700&display=swap" rel="stylesheet">
<style>
:root{
  --green:#4cb848;
  --green-dark:#3d9a3a;
  --blue:#3c8fd0;
  --ink:#333;
  --muted:#777;
  --page:#ecf4f7;
  --card:#fff;
  --line:#dfe5e8;
  --footer:#4a4a48;
  --footer-line:#5d5d5a;
}
*{margin:0;padding:0;box-sizing:border-box}
html,body{width:926px;height:1200px;overflow:hidden}
body{background:var(--page);font-family:"Raleway",sans-serif;color:var(--ink);position:relative}
.abs{position:absolute}
.display{font-family:"Lilita One",sans-serif;font-weight:400}

/* hero */
.hero{left:0;top:0;width:926px;height:350px;background:linear-gradient(180deg,#1d3a4a 0%,#2f5a5a 35%,#4f7c3a 70%,#3f7a22 100%);overflow:hidden}
.hero-glow{left:0;top:0;width:926px;height:350px;background:radial-gradient(ellipse at 20% 30%,rgba(140,180,200,.35),transparent 55%),radial-gradient(ellipse at 85% 25%,rgba(120,170,120,.3),transparent 50%)}
.hero-edge{left:0;top:318px;width:926px;height:40px}
.brand{left:155px;top:12px;display:flex;align-items:center;gap:8px;color:#fff;font-size:21px;letter-spacing:.5px}
.brand-dot{width:22px;height:22px;border-radius:50%;background:#fff}
.nav{left:429px;top:19px;display:flex;gap:14px;font-family:"Open Sans",sans-serif;font-size:8.5px;font-weight:600;color:#fff;letter-spacing:.3px}
.nav .active{color:var(--green)}
.nav-btn{top:15px;height:18px;border-radius:2px;color:#fff;font-family:"Open Sans",sans-serif;font-size:8px;font-weight:600;display:flex;align-items:center;gap:5px;padding:0 8px}
.nav-btn.register{left:658px;width:61px;background:var(--green)}
.nav-btn.login{left:724px;width:48px;background:var(--blue)}
.nav-rule{left:154px;top:46px;width:617px;height:1px;background:rgba(255,255,255,.25)}
.headline{left:0;top:68px;width:926px;text-align:center;color:#fff;font-size:27px;letter-spacing:.5px}

.post{top:310px;width:14px;height:42px;background:linear-gradient(90deg,#b86a1e,#e08a2e,#b86a1e)}
.board{left:161px;top:122px;width:603px;height:193px;background:#fff;box-shadow:0 3px 8px rgba(0,0,0,.3)}
.board-photo{left:7px;top:7px;width:589px;height:179px;background:linear-gradient(90deg,#6e7a72 0%,#b9c3bd 35%,#8ea3a0 55%,#3f4a4c 75%,#7d9a6a 100%)}
.join{left:22px;top:22px;width:237px;height:149px;background:rgba(236,236,236,.92);text-align:center;padding-top:28px}
.join h2{font-size:22px;color:#2c2c2c;margin-bottom:10px}
.join p{font-size:8.6px;line-height:12.5px;color:#444;padding:0 14px}
.dots{left:620px;top:293px;display:flex;gap:2px}
.dots i{width:4px;height:4px;border-radius:50%;border:1px solid #fff}

/* cards */
.card{background:var(--card);border:1px solid var(--line);border-radius:2px}
.section-title{font-size:12.5px;color:var(--green);letter-spacing:.3px}
.howto{left:154px;top:373px;width:617px;height:109px}
.step{top:36px;width:200px}
.step-num{font-size:30px;color:var(--blue);line-height:1}
.step-name{font-size:12px;color:var(--blue);margin-left:4px}
.step p{font-size:7.6px;line-height:12px;color:#555;margin-top:6px}

.featured{left:154px;top:500px;width:416px;height:344px}
.match{width:186px;height:136px}
.team{top:16px;width:70px;text-align:center;font-family:"Open Sans",sans-serif;font-size:8.3px;line-height:10px;color:#444}
.crest{width:40px;height:46px;margin:0 auto 8px;border-radius:6px 6px 20px 20px;background:#cfd8dc}
.vs{left:81px;top:38px;width:20px;height:20px;border-radius:50%;background:var(--blue);border:2px solid #cfe3f3;color:#fff;font-family:"Open Sans",sans-serif;font-size:6.5px;font-weight:700;display:flex;align-items:center;justify-content:center}
.btn{background:var(--green);color:#fff;font-family:"Open Sans",sans-serif;font-weight:700;font-size:9.5px;display:flex;align-items:center;justify-content:center;border-radius:2px}
.match .btn{left:29px;top:97px;width:127px;height:24px}

.winner{left:154px;top:862px;width:420px;height:36px}
.winner-title{left:0;top:4px;font-size:12.5px;color:#333}
.winner-title span{color:var(--blue)}
.winner-item{top:0;display:flex;gap:8px;align-items:flex-start}
.avatar{width:32px;height:32px;border-radius:50%;background:radial-gradient(circle at 50% 40%,#d9b79a,#8b6a52);border:2px solid #fff;box-shadow:0 0 0 1px #ddd}
.winner-item .name{font-size:8.5px;color:#999;margin-top:3px}
.winner-item .prize{font-size:8.5px;color:var(--green)}

.signup{left:587px;top:500px;width:184px;height:177px}
.field{left:13px;width:158px;height:22px;border:1px solid #e2e6e8;background:#f9fafa;font-size:7.5px;color:#aaa;padding:7px 7px 0}
.agree{left:13px;top:120px;display:flex;align-items:center;gap:5px;font-size:6.6px;color:#999}
.signup .btn{left:13px;top:143px;width:158px;height:23px}

.fans{left:587px;top:697px;width:184px;height:201px}
.fan-page{left:8px;top:36px;display:flex;gap:6px}
.fan-logo{width:20px;height:20px;background:#e24b7a}
.fan-name{font-family:"Open Sans",sans-serif;font-size:7px;font-weight:700;color:#3b5b98}
.like{margin-top:3px;width:25px;height:9px;background:#4c6fb0;color:#fff;font-size:5.5px;font-weight:700;display:flex;align-items:center;justify-content:center;font-family:"Open Sans",sans-serif}
.fan-rule{left:8px;top:64px;width:166px;height:1px;background:#e4e4e4}
.fan-count{left:8px;top:68px;font-family:"Open Sans",sans-serif;font-size:6px;font-weight:700;color:#333}
.fan-count span{color:#3b5b98}
.fan-grid{left:10px;top:79px;width:162px;height:110px;background:linear-gradient(135deg,#8a8f95,#6f5a4c 40%,#4b6d7a 70%,#2f2f33)}

.divider{left:154px;top:918px;width:617px;height:3px;background:linear-gradient(90deg,transparent,#d5dde0,transparent)}
.about-title{left:0;top:940px;width:926px;text-align:center;font-size:17px;color:#333}
.about-title span{color:var(--blue)}
.about-text{left:150px;top:968px;width:626px;text-align:center;font-size:7.6px;line-height:13.5px;color:#888}
.about-text a{color:var(--blue);text-decoration:none}

.treeline{left:0;top:1016px;width:926px;height:42px}
.footer{left:0;top:1054px;width:926px;height:146px;background:var(--footer)}
.sub-label{left:0;top:16px;width:926px;text-align:center;font-size:7.8px;color:var(--green)}
.sub-input{left:377px;top:29px;width:116px;height:23px;background:#fff;border-radius:2px;font-size:7.5px;color:#555;padding:7px 9px 0}
.sub-btn{left:499px;top:29px;width:55px;height:23px}
.foot-links{left:0;top:64px;width:926px;text-align:center;font-size:8px;color:#ddd;word-spacing:1px}
.foot-links span{margin:0 4px}
.social{left:436px;top:82px;display:flex;gap:4px}
.social i{width:16px;height:16px;border-radius:50%;background:#fff}
.foot-rule{left:154px;top:112px;width:617px;height:1px;background:var(--footer-line)}
.copy{left:0;top:122px;width:926px;text-align:center;font-size:7.8px;color:#ddd}
</style>
</head>
<body>

<header class="abs hero">
  <div class="abs hero-glow"></div>
  <svg class="abs hero-edge" viewBox="0 0 926 40" preserveAspectRatio="none" aria-hidden="true">
    <path d="M0 12 Q15 0 30 12 Q45 26 62 14 Q80 2 96 16 Q112 28 130 18 Q148 6 166 20 L166 40 L0 40 Z M760 20 Q778 6 796 18 Q814 28 830 16 Q846 2 864 14 Q881 26 896 12 Q911 0 926 12 L926 40 L760 40 Z M166 20 Q200 30 240 26 Q300 32 360 30 L560 30 Q640 32 700 26 Q740 30 760 20 L760 40 L166 40 Z" fill="#ecf4f7"/>
  </svg>
</header>

<div class="abs brand display"><span class="brand-dot"></span>PITCHTALLY</div>
<nav class="abs nav">
  <span class="active">HOME</span><span>MINILIGA</span><span>TABLES</span><span>KITTY</span><span>FAQ</span><span>ME</span>
</nav>
<div class="abs nav-btn register"><svg width="7" height="8" viewBox="0 0 7 8"><rect x="0" y="3.5" width="7" height="4.5" fill="#fff"/><path d="M1.5 3.5V2a2 2 0 0 1 4 0v1.5" stroke="#fff" fill="none"/></svg>REGISTER</div>
<div class="abs nav-btn login"><svg width="8" height="8" viewBox="0 0 8 8"><path d="M4 1h3v6H4M0 4h5M3 2l2 2-2 2" stroke="#fff" fill="none"/></svg>LOGIN</div>
<div class="abs nav-rule"></div>
<h1 class="abs headline display">ALTOGETHER BETTER PREDICTIONS</h1>

<div class="abs post" style="left:351px"></div>
<div class="abs post" style="left:557px"></div>
<div class="abs board">
  <div class="abs board-photo" role="img" aria-label="Photo of a smiling man in a suit holding a tablet outdoors"></div>
  <div class="abs join">
    <h2 class="display">Join Us</h2>
    <p>Predict results, scores and scorers for your free chance to win a £20 Shopwell voucher every week. Overall season winner gets up to £1000 in Shopwell vouchers! No entry fee and no catches.</p>
  </div>
</div>
<div class="abs dots"><i></i><i></i><i></i><i></i></div>

<section class="abs card howto">
  <h3 class="abs section-title display" style="left:12px;top:10px">HOW TO PLAY</h3>
  <div class="abs step" style="left:12px"><span class="step-num display">01.</span><span class="step-name display">LOGIN</span><p>Lorem ipsum dolor sit amet, consectetur adipiscing elit. Aliquam semper nisi et ullamcorper blandit.</p></div>
  <div class="abs step" style="left:225px"><span class="step-num display">02.</span><span class="step-name display">PREDICT</span><p>Lorem ipsum dolor sit amet, consectetur adipiscing elit. Aliquam semper nisi et ullamcorper blandit.</p></div>
  <div class="abs step" style="left:426px"><span class="step-num display">03.</span><span class="step-name display">ENJOY</span><p>Lorem ipsum dolor sit amet, consectetur adipiscing elit. Aliquam semper nisi et ullamcorper blandit.</p></div>
</section>

<section class="abs card featured">
  <h3 class="abs section-title display" style="left:12px;top:14px">FEATURED PREDICTIONS</h3>
  <div class="abs card match" style="left:14px;top:42px">
    <div class="abs team" style="left:8px"><div class="crest" style="background:#e8cf5a"></div>ASHFORD VALE</div>
    <div class="abs vs">VS</div>
    <div class="abs team" style="left:108px"><div class="crest" style="background:#a9c3e4"></div>KINGSMERE PARK ROVERS</div>
    <div class="abs btn">PREDICT SCORE NOW</div>
  </div>
  <div class="abs card match" style="left:214px;top:42px">
    <div class="abs team" style="left:8px"><div class="crest" style="background:#2f5fb0;border-radius:50%"></div>HARBOURSIDE</div>
    <div class="abs vs">VS</div>
    <div class="abs team" style="left:108px"><div class="crest" style="background:#3a3a3a"></div>NORTHGATE UNITED</div>
    <div class="abs btn">PREDICT SCORE NOW</div>
  </div>
  <div class="abs card match" style="left:14px;top:193px">
    <div class="abs team" style="left:8px"><div class="crest" style="background:#2f55a8"></div>GLASS HILL</div>
    <div class="abs vs">VS</div>
    <div class="abs team" style="left:108px"><div class="crest" style="background:#1f2a4a"></div>EASTBROOK ROVERS</div>
    <div class="abs btn">PREDICT SCORE NOW</div>
  </div>
  <div class="abs card match" style="left:214px;top:193px">
    <div class="abs team" style="left:8px"><div class="crest" style="background:#2a2a2a;border-radius:50%"></div>BAYPORT CITY</div>
    <div class="abs vs">VS</div>
    <div class="abs team" style="left:108px"><div class="crest" style="background:#e8cf5a"></div>RIVERSIDE UNITED</div>
    <div class="abs btn">PREDICT SCORE NOW</div>
  </div>
</section>

<section class="abs winner">
  <div class="abs winner-title display">RECENT <span>WINNER</span> <span>›</span></div>
  <div class="abs winner-item" style="left:116px"><div class="avatar" role="img" aria-label="Winner profile photo"></div><div><div class="name">Sammy88</div><div class="prize">£30.32</div></div></div>
  <div class="abs winner-item" style="left:223px"><div class="avatar" role="img" aria-label="Winner profile photo"></div><div><div class="name">Sammy88</div><div class="prize">£30.32</div></div></div>
  <div class="abs winner-item" style="left:333px"><div class="avatar" role="img" aria-label="Winner profile photo"></div><div><div class="name">Sammy88</div><div class="prize">£30.32</div></div></div>
</section>

<aside class="abs card signup">
  <h3 class="abs section-title display" style="left:13px;top:14px">FREE SIGN UP!</h3>
  <div class="abs field" style="top:38px">Username*</div>
  <div class="abs field" style="top:65px">E-mail*</div>
  <div class="abs field" style="top:93px">Password*</div>
  <div class="abs agree"><svg width="11" height="10" viewBox="0 0 11 10"><path d="M1 5l3 3 6-7" stroke="#3c8fd0" stroke-width="2" fill="none"/></svg>I agree with the General Terms &amp; Conditions*</div>
  <div class="abs btn">CREATE MY ACCOUNT</div>
</aside>

<aside class="abs card fans">
  <h3 class="abs section-title display" style="left:10px;top:12px">FANBOOK FANS</h3>
  <div class="abs fan-page"><div class="fan-logo"></div><div><div class="fan-name">Corner Market</div><div class="like">Like</div></div></div>
  <div class="abs fan-rule"></div>
  <div class="abs fan-count">1,913 people like <span>Corner Market.</span></div>
  <div class="abs fan-grid" role="img" aria-label="Grid of fan profile photos"></div>
</aside>

<div class="abs divider"></div>
<h2 class="abs about-title display">ABOUT <span>PITCHTALLY</span></h2>
<p class="abs about-text">Lorem ipsum dolor sit amet, consectetur adipiscing elit. Aliquam semper nisi et ullamcorper blandit. Fusce nec quam eu nibh volutpat mollis at vel orci. Suspendisse potenti. Morbi in sapien vestibulum dui finibus consectetur. Sed eget elit non tellus aliquet dignissim. Sed non augue ex. Suspendisse nisi lacus, posuere id placerat. <a href="#">read more...</a></p>

<svg class="abs treeline" viewBox="0 0 926 42" preserveAspectRatio="none" role="img" aria-label="Illustrated row of green trees and hills">
  <path d="M0 26 Q120 18 240 24 T480 22 T720 24 T926 20 L926 42 L0 42 Z" fill="#8cc63f"/>
  <path d="M0 32 Q150 26 300 32 T600 30 T926 28 L926 42 L0 42 Z" fill="#6aa832"/>
</svg>

<footer class="abs footer">
  <div class="abs sub-label">Subscribe to exclusive auctions</div>
  <div class="abs sub-input">Email Address</div>
  <div class="abs btn sub-btn">SUBMIT</div>
  <div class="abs foot-links"><span>Accessibility</span><span>Privacy and Cookies Notice</span><span>Terms and Conditions</span><span>Recover Details</span><span>Links</span><span>Account FAQs</span><span>Games FAQs</span></div>
  <div class="abs social" aria-label="Social links"><i></i><i></i><i></i></div>
  <div class="abs foot-rule"></div>
  <div class="abs copy">© PitchTally 2015. All rights reserved.</div>
</footer>

</body>
</html>
```